Halverns Facebook Promo

I am a singer and have a number of shows throughout 2025 that I would like to promote on Facebook, to help raise my profile and also to share on my clients social media pages. I therefore need two separate promotions suitable for Facebook : 1st - Simply As Oswin 2nd - Tam Rushko's Stay Close Tonight - All the Dorsey Kellum Classics -Each promo is to include a few logos, photo, the date and venue so that I can actively support the promotion. Please refer to the attached word document for more info.

```html
<!DOCTYPE html>
<html lang="en">
<head>
<meta charset="utf-8">
<title>Tam Rushko – Stay Close Tonight</title>
<link rel="stylesheet" href="https://fonts.googleapis.com/css2?family=Montserrat:wght@600;700;800;900&display=swap">
<style>
  :root {
    --bg: #000000;
    --white: #ffffff;
    --fire-top: #ffd21a;
    --fire-mid: #ff7a12;
    --fire-low: #ff2a12;
    --navy: #173a55;
    --denim: #3b5a7a;
    --skin: #5a3a2a;
    --pink: #e2369a;
  }
  * { margin: 0; padding: 0; box-sizing: border-box; }
  html, body { width: 1200px; height: 1200px; overflow: hidden; background: var(--bg); }
  .poster {
    position: relative;
    width: 1200px;
    height: 1200px;
    background: var(--bg);
    font-family: "Montserrat", sans-serif;
    color: var(--white);
    overflow: hidden;
  }
  .line {
    position: absolute;
    left: 0;
    width: 100%;
    text-align: center;
    white-space: nowrap;
  }
  .fire-text {
    background: linear-gradient(180deg, var(--fire-top) 0%, var(--fire-mid) 50%, var(--fire-low) 100%);
    -webkit-background-clip: text;
    background-clip: text;
    color: transparent;
  }
  .artist-name {
    top: 20px;
    font-weight: 900;
    font-size: 122px;
    line-height: 1.05;
  }
  .performer-photo {
    position: absolute;
    top: 150px;
    left: 90px;
    width: 1020px;
    height: 600px;
    background:
      radial-gradient(ellipse 22% 30% at 50% 30%, var(--skin) 0%, rgba(90,58,42,0) 100%),
      radial-gradient(ellipse 48% 55% at 50% 75%, var(--denim) 0%, rgba(59,90,122,0) 100%),
      var(--bg);
  }
  .show-title {
    top: 752px;
    font-weight: 900;
    font-size: 92px;
    line-height: 1;
    letter-spacing: -1px;
  }
  .show-subtitle {
    top: 862px;
    font-weight: 800;
    font-size: 56px;
    line-height: 1;
  }
  .show-details {
    top: 942px;
    font-weight: 700;
    font-size: 42px;
    line-height: 1.15;
  }
  .contact {
    top: 1104px;
    font-weight: 700;
    font-size: 34px;
    line-height: 1.2;
  }
  .venue-mark {
    position: absolute;
    left: 37px;
    top: 1030px;
    width: 140px;
    height: 138px;
    background: var(--navy);
    border: 4px solid var(--white);
    display: flex;
    flex-direction: column;
    align-items: center;
    justify-content: center;
    gap: 12px;
  }
  .venue-mark .dot {
    width: 30px;
    height: 30px;
    border-radius: 50%;
    background: var(--white);
  }
  .venue-mark .name {
    font-weight: 700;
    font-size: 19px;
    color: var(--white);
    letter-spacing: 0.5px;
  }
  .agency-mark {
    position: absolute;
    right: 28px;
    top: 1072px;
    width: 240px;
    text-align: center;
    font-weight: 800;
    font-size: 38px;
    color: var(--pink);
  }
</style>
</head>
<body>
  <main class="poster">
    <h1 class="line artist-name fire-text">TAM RUSHKO</h1>

    <div class="performer-photo" role="img" aria-label="Photo of the singer in a red beanie and embellished denim jacket, arms folded, holding a microphone against a black background"></div>

    <h2 class="line show-title">STAY CLOSE TONIGHT</h2>
    <p class="line show-subtitle">ALL THE <span class="fire-text">DORSEY KELLUM</span> CLASSIC</p>

    <p class="line show-details">Monday 12th May 2025<br>Halverns Hotels, Ashcombe Park</p>

    <p class="line contact">Contact : hello@brightvista.com</p>

    <div class="venue-mark" aria-label="Halverns Hotels">
      <span class="dot"></span>
      <span class="name">HALVERNS</span>
    </div>

    <div class="agency-mark">Brightvista</div>
  </main>
</body>
</html>
```